QuillBarn23' Website/Logo Design

We need a website and Logo design for our company called "quillbarn7823". We will be designing generic and mainly custom made clothing (t shirts, sweaters, hoodies, hats, caps, leggings etc) with other products of electronics and every day products with side sells. We want a catchy but easy to navigate website to use on our SHOPIFY website.
Updates

Designs look the same

Target Market(s)

Anyone that is interested in purchasing custom design clothing.

Logo Text

QuillBarn23'

Number of Pages Required

1 page

Other font styles liked:
• Microbrew

Colors

Designer to choose colors to be used in the design.

```html
<!DOCTYPE html>
<html lang="en">
<head>
<meta charset="utf-8">
<title>QuillBarn23' — Shop</title>
<link href="https://fonts.googleapis.com/css2?family=Roboto:wght@400;500;700;900&family=Roboto+Condensed:wght@700&display=swap" rel="stylesheet">
<style>
:root{
  --accent:#e4532a;
  --ink:#2b2b2b;
  --muted:#6b6b6b;
  --line:#dcdcdc;
  --soft:#f3f3f3;
  --band:#3a3a3a;
  --foot:#2e2e2e;
  --white:#ffffff;
}
*{box-sizing:border-box;margin:0;padding:0}
html,body{width:1200px;height:3237px;overflow:hidden}
body{position:relative;background:var(--white);font-family:"Roboto",Arial,sans-serif;color:var(--ink)}
.abs{position:absolute}
a{color:inherit;text-decoration:none}

/* top utility bar */
.utility{top:0;left:0;width:1200px;height:32px;border-bottom:1px solid var(--line);display:flex;justify-content:flex-end;align-items:center;gap:26px;padding-right:162px;font-size:10px;font-weight:500;text-transform:uppercase;color:#444}
.utility span{display:flex;align-items:center;gap:5px}
.utility svg{width:10px;height:10px}

/* header */
.header{top:32px;left:0;width:1200px;height:65px;display:flex;align-items:center;padding:0 162px}
.brand{display:flex;align-items:center;gap:10px;font-weight:700;font-size:20px;color:var(--ink)}
.brand-dot{width:30px;height:30px;background:var(--ink);border-radius:50%}
.nav{display:flex;gap:32px;margin-left:auto;margin-right:46px;font-size:12.5px;font-weight:700;text-transform:uppercase;height:65px;align-items:center}
.nav a{height:65px;display:flex;align-items:center;border-bottom:3px solid transparent}
.nav a.active{border-bottom-color:var(--ink)}
.search{width:216px;height:34px;border:1px solid #cfcfcf;display:flex;align-items:center;justify-content:space-between;padding:0 10px;font-size:10.5px;color:#888}

/* hero */
.hero{top:97px;left:0;width:1200px;height:410px;background:linear-gradient(90deg,#f2f2f2 0%,#e4e2e0 45%,#c9b8b3 62%,#a49894 80%,#cfcbc8 100%)}
.hero-copy{position:absolute;left:162px;top:112px}
.hero-kicker{font-size:17px;letter-spacing:1px;color:#555}
.hero-title{font-family:"Roboto Condensed",Arial,sans-serif;font-size:104px;line-height:.9;font-weight:700;letter-spacing:-2px;color:#1f1f1f;margin-top:4px}
.hero-offer{margin-top:16px;border-top:2px solid #333;border-bottom:2px solid #333;padding:5px 0;width:384px;font-size:24px;font-weight:900;color:#222}
.hero-offer small{font-size:11px;font-weight:500;letter-spacing:1px;color:#555;margin-left:8px}
.btn{display:inline-block;background:var(--accent);color:var(--white);font-weight:700;text-transform:uppercase;font-size:13px}
.hero-btn{margin-top:32px;width:110px;height:33px;line-height:33px;text-align:center}
.dots{display:flex;gap:6px}
.dots i{width:7px;height:7px;border-radius:50%;background:#555}
.dots i:first-child{background:var(--accent)}
.hero-dots{position:absolute;left:162px;top:372px}

/* section titles */
.title{left:0;width:1200px;text-align:center;font-size:23px;font-weight:700;text-transform:uppercase}
.title::after{content:"";display:block;width:18px;height:2px;background:var(--ink);margin:9px auto 0}

.arrow{width:16px;height:16px}

/* shop by */
.shop-by{top:619px;left:162px;width:876px;height:266px;display:flex;gap:8px}
.cat{border:1px solid #d6d6d6;padding:11px;position:relative}
.cat .photo{width:100%;height:100%}
.cat-label{position:absolute;background:var(--white);font-family:"Roboto Condensed",Arial,sans-serif;font-weight:700;font-size:38px;padding:6px 16px;color:var(--ink)}

/* product tiles */
.tiles{top:1001px;left:162px;width:876px;height:313px;display:flex;gap:14px}
.tile{flex:1;position:relative}
.tile .photo{width:100%;height:100%}
.tile-label{position:absolute;left:0;bottom:22px;background:var(--white);font-size:23px;font-weight:700;padding:10px 22px 10px 22px;text-transform:uppercase}

/* deals */
.deals-head{top:1390px;left:162px;width:876px;height:30px;display:flex;align-items:center}
.deals-head h2{font-size:23px;font-weight:700;text-transform:uppercase}
.timer{margin-left:26px;font-size:12.5px;color:#444;display:flex;align-items:center;gap:5px}
.view-all{margin-left:auto;width:70px;height:22px;line-height:22px;text-align:center;font-size:10px}
.grid{left:162px;width:876px;display:grid;gap:0 16px}
.grid-4{grid-template-columns:repeat(4,1fr)}
.grid-5{grid-template-columns:repeat(5,1fr);gap:0 10px}
.card .photo{position:relative}
.card h3{font-size:13px;font-weight:700;text-transform:uppercase;margin-top:16px;color:#333}
.card p{font-size:9.5px;text-transform:uppercase;color:#555;margin-top:1px}
.price{font-size:26px;font-weight:700;margin-top:6px}
.sm h3{font-size:12px;font-weight:500;margin-top:20px}
.sm .price{font-size:17px;margin-top:6px}
.sm .price s{font-size:15px;font-weight:500;color:#777;margin-left:20px}
.tag{position:absolute;left:15px;top:13px;background:var(--accent);color:var(--white);font-size:9px;font-weight:700;padding:3px 6px}
.stock{position:absolute;left:0;right:0;top:72px;height:34px;line-height:34px;background:rgba(255,255,255,.85);text-align:center;font-size:12px;font-weight:500}
.divider-band{left:162px;width:876px;height:26px;background:linear-gradient(#f0f0f0,#fff)}

/* subscribe */
.subscribe{top:2493px;left:0;width:1200px;height:110px;background:var(--band);color:var(--white)}
.sub-copy{position:absolute;left:188px;top:30px;display:flex;gap:20px;align-items:center}
.sub-copy .small{font-size:17px;letter-spacing:.5px;color:#ddd}
.sub-copy .big{font-size:23px;font-weight:700;text-transform:uppercase}
.sub-rule{position:absolute;left:529px;top:18px;width:1px;height:74px;background:#777}
.sub-input{position:absolute;left:555px;top:37px;width:336px;height:36px;background:var(--white);color:#777;font-size:11px;padding:12px 16px;text-transform:uppercase}
.sub-btn{position:absolute;left:896px;top:37px;width:114px;height:36px;line-height:36px;text-align:center}

/* features */
.feature{top:2650px;width:200px;text-align:center}
.feature h4{font-size:13px;font-weight:700;text-transform:uppercase;margin-top:6px}
.feature p{font-size:11px;color:#555;margin-top:3px}
.badge{top:2661px;width:94px;height:32px;background:#111;border-radius:5px}

/* footer */
.foot-rule{left:0;width:1200px;height:1px;background:var(--line)}
.foot-col{top:2806px}
.foot-col h5{font-size:15px;font-weight:700;text-transform:uppercase;margin-bottom:16px}
.foot-col li{list-style:none;font-size:11.5px;color:#333;line-height:23.5px}
.social{display:grid;grid-template-columns:106px 94px;row-gap:14px;font-size:11px}
.social span{display:flex;align-items:center;gap:7px;white-space:nowrap}
.social i{width:30px;height:30px;flex:none;border-radius:50%;border:1.5px solid #3b5a9a}
.social .c2 i{border-color:#3da3dd}.social .c3 i{border-color:#d0357a}.social .c4 i{border-color:#d43b2c}
.rule-inner{left:162px;width:876px;height:1px;background:#555}
.contact{top:3040px;left:0;width:1200px;display:flex;justify-content:center;gap:180px;font-size:10.5px;color:#333}
.contact span{display:flex;gap:7px;align-items:center}
.pay{top:3116px;left:0;width:1200px;display:flex;justify-content:center;gap:4px}
.pay i{width:24px;height:15px;border:1px solid #ccc;border-radius:2px;background:#f4f4f4}
.pay i:nth-child(2){background:#f1c7b8}.pay i:nth-child(3){background:#c9d6ee}.pay i:nth-child(5){background:#f1dcc4}
.bottom{top:3168px;left:0;width:1200px;height:69px;background:var(--foot);color:#aaa;font-size:10px;text-align:center;line-height:69px;letter-spacing:.5px;text-transform:uppercase}
</style>
</head>
<body>

<div class="abs utility">
  <span><svg viewBox="0 0 10 10"><path d="M2 1l2 2-1 1a5 5 0 003 3l1-1 2 2-1 1C4 9 1 6 1 2z" fill="#444"/></svg>Contact us</span>
  <span><svg viewBox="0 0 10 10"><rect x="3" y="0.5" width="4" height="9" rx="1" fill="none" stroke="#444"/></svg>Download app</span>
  <span><svg viewBox="0 0 10 10"><path d="M5 0a3 3 0 013 3c0 2-3 7-3 7S2 5 2 3a3 3 0 013-3z" fill="#444"/></svg>Track order</span>
  <span><svg viewBox="0 0 10 10"><circle cx="5" cy="3" r="2.3" fill="#444"/><path d="M1 10a4 4 0 018 0z" fill="#444"/></svg>My account</span>
  <span><svg viewBox="0 0 10 10"><path d="M1 5h6M5 3l2 2-2 2M6 1h3v8H6" fill="none" stroke="#444"/></svg>Sign in</span>
  <span><svg viewBox="0 0 10 10"><path d="M1 9l1-3 5-5 2 2-5 5z" fill="#444"/></svg>Sign up</span>
  <span><svg viewBox="0 0 10 10"><path d="M1.5 3h7v6.5h-7zM3.5 3a1.5 1.5 0 013 0" fill="none" stroke="#444"/></svg>My bag</span>
</div>

<header class="abs header">
  <div class="brand"><span class="brand-dot"></span>QuillBarn23'</div>
  <nav class="nav">
    <a class="active">Women</a><a>Men</a><a>Kids</a><a>Accessories</a>
  </nav>
  <div class="search">What are you looking for today?
    <svg width="14" height="14" viewBox="0 0 14 14"><circle cx="6" cy="6" r="4.5" fill="none" stroke="#333" stroke-width="2"/><path d="M9.5 9.5L13 13" stroke="#333" stroke-width="2"/></svg>
  </div>
</header>

<section class="abs hero" role="img" aria-label="Woman in a pink knit beanie and mittens in falling snow against pale wooden boards">
  <div class="hero-copy">
    <div class="hero-kicker">CAN'T GET ENOUGH</div>
    <div class="hero-title">MINIMUM</div>
    <div class="hero-offer">30% - 70% OFF <small>( OVER 2,00,000 STYLES )</small></div>
    <a class="btn hero-btn">Shop now</a>
  </div>
  <div class="dots hero-dots"><i></i><i></i><i></i><i></i></div>
</section>

<h2 class="abs title" style="top:559px">Shop by</h2>
<svg class="abs arrow" style="left:126px;top:744px" viewBox="0 0 16 16"><path d="M10 3L5 8l5 5" fill="none" stroke="#333" stroke-width="2"/></svg>
<svg class="abs arrow" style="left:1058px;top:744px" viewBox="0 0 16 16"><path d="M6 3l5 5-5 5" fill="none" stroke="#333" stroke-width="2"/></svg>
<div class="abs shop-by">
  <div class="cat" style="width:451px">
    <div class="photo" role="img" aria-label="Young man with styled hair in a blazer" style="background:linear-gradient(90deg,#e6e4e1,#c7b7a9 60%,#8a7767)"></div>
    <span class="cat-label" style="left:32px;top:104px">MEN</span>
  </div>
  <div class="cat" style="width:210px">
    <div class="photo" role="img" aria-label="Smiling woman in sunglasses with hair blowing" style="background:linear-gradient(160deg,#d5d2cf,#a39b96 60%,#6d625c)"></div>
    <span class="cat-label" style="left:18px;top:190px">WOMEN</span>
  </div>
  <div class="cat" style="width:199px">
    <div class="photo" role="img" aria-label="Smiling girl wearing white ear muffs" style="background:linear-gradient(160deg,#d9a982,#b67a53 60%,#8d5a3e)"></div>
    <span class="cat-label" style="left:18px;top:190px">KIDS</span>
  </div>
</div>

<h2 class="abs title" style="top:941px">Shop by product</h2>
<div class="abs tiles">
  <div class="tile"><div class="photo" role="img" aria-label="Stack of folded knit sweaters on wooden boards" style="background:linear-gradient(135deg,#8d8f9a,#5f6270 50%,#a0866b)"></div><span class="tile-label">Sweaters</span></div>
  <div class="tile"><div class="photo" role="img" aria-label="White printed t-shirt on a hanger against dark wood" style="background:linear-gradient(90deg,#5a3d2d,#e8e6e3 40%,#e8e6e3 60%,#5a3d2d)"></div><span class="tile-label">T shirts</span></div>
  <div class="tile"><div class="photo" role="img" aria-label="Woman in pink leggings stretching outdoors" style="background:linear-gradient(180deg,#c9d0d6,#b6b8b8 55%,#d04a9a 80%,#8a8580)"></div><span class="tile-label">Leggings</span></div>
</div>
<div class="abs dots" style="left:579px;top:1350px"><i></i><i></i><i></i><i></i></div>

<div class="abs deals-head">
  <h2>Deals of the day</h2>
  <span class="timer"><svg width="12" height="12" viewBox="0 0 12 12"><circle cx="6" cy="6" r="5" fill="none" stroke="#444" stroke-width="1.4"/><path d="M6 3v3l2 1" fill="none" stroke="#444" stroke-width="1.4"/></svg>17 : 20 : 51 LEFT</span>
  <a class="btn view-all">View all</a>
</div>
<svg class="abs arrow" style="left:126px;top:1525px" viewBox="0 0 16 16"><path d="M10 3L5 8l5 5" fill="none" stroke="#333" stroke-width="2"/></svg>
<svg class="abs arrow" style="left:1058px;top:1525px" viewBox="0 0 16 16"><path d="M6 3l5 5-5 5" fill="none" stroke="#333" stroke-width="2"/></svg>
<div class="abs grid grid-4" style="top:1440px">
  <div class="card"><div class="photo" role="img" aria-label="Black patterned leggings against a red brick wall" style="height:194px;background:linear-gradient(135deg,#8c2d25,#3a2a2a 55%,#9b3a2c)"></div><h3>Quisque pharetra</h3><p>Maecenas vitae tellus scelerisque</p><div class="price">$35.00</div></div>
  <div class="card"><div class="photo" role="img" aria-label="Two straw sun hats with black bands" style="height:194px;background:linear-gradient(135deg,#c8d6e0,#d9c39b 55%,#b8c7d2)"></div><h3>Quisque pharetra</h3><p>Maecenas vitae tellus scelerisque</p><div class="price">$35.00</div></div>
  <div class="card"><div class="photo" role="img" aria-label="Grey hoodie with white drawstrings" style="height:194px;background:linear-gradient(135deg,#c4c4c4,#9e9e9e 60%,#d2d2d2)"></div><h3>Quisque pharetra</h3><p>Maecenas vitae tellus scelerisque</p><div class="price">$35.00</div></div>
  <div class="card"><div class="photo" role="img" aria-label="Plain white t-shirt on a hanger against a dark brick wall" style="height:194px;background:linear-gradient(90deg,#2f3337,#e9e9e9 45%,#e9e9e9 55%,#2f3337)"></div><h3>Quisque pharetra</h3><p>Maecenas vitae tellus scelerisque</p><div class="price">$35.00</div></div>
</div>

<div class="abs divider-band" style="top:1759px"></div>
<h2 class="abs title" style="top:1800px">New arrivals</h2>
<svg class="abs arrow" style="left:126px;top:1931px" viewBox="0 0 16 16"><path d="M10 3L5 8l5 5" fill="none" stroke="#333" stroke-width="2"/></svg>
<svg class="abs arrow" style="left:1058px;top:1931px" viewBox="0 0 16 16"><path d="M6 3l5 5-5 5" fill="none" stroke="#333" stroke-width="2"/></svg>
<div class="abs grid grid-5" style="top:1858px">
  <div class="card sm"><div class="photo" role="img" aria-label="Colourful folded t-shirts fanned out" style="height:158px;background:linear-gradient(135deg,#e83a7a,#f4d23a 35%,#3aa0e0 65%,#5ac25a)"></div><h3>Maecenas vitae</h3><div class="price">$20.00<s>27.00</s></div></div>
  <div class="card sm"><div class="photo" role="img" aria-label="Pink sunglasses on sand" style="height:158px;background:linear-gradient(135deg,#e2c49d,#e0519a 50%,#d9b98d)"></div><h3>Maecenas vitae</h3><div class="price">$20.00<s>27.00</s></div></div>
  <div class="card sm"><div class="photo" role="img" aria-label="Stack of folded knitwear" style="height:158px;background:linear-gradient(180deg,#dedbd7,#a9a39d 55%,#d8d2cc)"><span class="tag">SALE</span></div><h3>Maecenas vitae</h3><div class="price">$20.00<s>27.00</s></div></div>
  <div class="card sm"><div class="photo" role="img" aria-label="Man in a denim jacket over a white tee" style="height:158px;background:linear-gradient(180deg,#3e4144,#5d7490 60%,#2f3236)"></div><h3>Maecenas vitae</h3><div class="price">$20.00<s>27.00</s></div></div>
  <div class="card sm"><div class="photo" role="img" aria-label="Woman in a plain white t-shirt" style="height:158px;background:linear-gradient(180deg,#3a3a3a,#e6e4e2 55%,#3a3a3a)"></div><h3>Maecenas vitae</h3><div class="price">$20.00<s>27.00</s></div></div>
</div>

<div class="abs divider-band" style="top:2126px"></div>
<h2 class="abs title" style="top:2169px">Best sellers</h2>
<svg class="abs arrow" style="left:126px;top:2290px" viewBox="0 0 16 16"><path d="M10 3L5 8l5 5" fill="none" stroke="#333" stroke-width="2"/></svg>
<svg class="abs arrow" style="left:1058px;top:2290px" viewBox="0 0 16 16"><path d="M6 3l5 5-5 5" fill="none" stroke="#333" stroke-width="2"/></svg>
<div class="abs grid grid-5" style="top:2225px">
  <div class="card sm"><div class="photo" role="img" aria-label="Runner in black and neon sports leggings" style="height:158px;background:linear-gradient(180deg,#b8c96a,#2b2d2f 45%,#6e7378)"></div><h3>Maecenas vitae</h3><div class="price">$20.00</div></div>
  <div class="card sm"><div class="photo" role="img" aria-label="Man in a grey t-shirt" style="height:158px;background:linear-gradient(180deg,#5b5650,#8f8f8f 55%,#3c3a38)"></div><h3>Maecenas vitae</h3><div class="price">$20.00</div></div>
  <div class="card sm"><div class="photo" role="img" aria-label="Black cap on a wooden surface" style="height:158px;background:linear-gradient(180deg,#8a7e74,#2a2a2a 50%,#9a8e82)"><span class="stock">OUT OF STOCK</span></div><h3>Maecenas vitae</h3><div class="price">$20.00</div></div>
  <div class="card sm"><div class="photo" role="img" aria-label="Straw cowboy hat with a red bandana" style="height:158px;background:linear-gradient(135deg,#8c8478,#e4d8c0 45%,#c1272d 75%,#7a6f64)"></div><h3>Maecenas vitae</h3><div class="price">$20.00</div></div>
  <div class="card sm"><div class="photo" role="img" aria-label="Woman in a white top and black leggings" style="height:158px;background:linear-gradient(180deg,#3b3b3b,#e6e6e6 40%,#1f1f1f 70%,#3b3b3b)"></div><h3>Maecenas vitae</h3><div class="price">$20.00</div></div>
</div>

<section class="abs subscribe">
  <div class="sub-copy">
    <svg width="60" height="50" viewBox="0 0 60 50"><path d="M30 2L58 22V48H2V22z" fill="#fff"/><path d="M2 22l28 18 28-18" fill="none" stroke="#3a3a3a" stroke-width="3"/></svg>
    <div><div class="small">SUBSCRIBE TO</div><div class="big">Receive our updates</div></div>
  </div>
  <div class="sub-rule"></div>
  <div class="sub-input">Your email</div>
  <a class="btn sub-btn">Subscribe</a>
</section>

<div class="abs feature" style="left:150px">
  <svg width="22" height="22" viewBox="0 0 22 22"><path d="M11 2l8 4v10l-8 4-8-4V6zM3 6l8 4 8-4M11 10v10" fill="none" stroke="#333" stroke-width="1.5"/></svg>
  <h4>Free returns</h4><p>Maecenas tellus scelerisque</p>
</div>
<div class="abs feature" style="left:362px">
  <svg width="26" height="22" viewBox="0 0 26 22"><path d="M2 5h14v11H2zM16 9h5l3 4v3h-8" fill="none" stroke="#333" stroke-width="1.5"/><circle cx="7" cy="17" r="2.2" fill="#fff" stroke="#333" stroke-width="1.5"/><circle cx="19" cy="17" r="2.2" fill="#fff" stroke="#333" stroke-width="1.5"/></svg>
  <h4>Fast delivery</h4><p>Maecenas tellus scelerisque</p>
</div>
<div class="abs feature" style="left:571px">
  <svg width="26" height="22" viewBox="0 0 26 22"><rect x="2" y="4" width="22" height="15" rx="2" fill="none" stroke="#333" stroke-width="1.5"/><path d="M2 9h22" stroke="#333" stroke-width="2.5"/></svg>
  <h4>Secure payments</h4><p>Maecenas tellus scelerisque</p>
</div>
<div class="abs badge" style="left:803px"></div>
<div class="abs badge" style="left:945px"></div>

<div class="abs foot-rule" style="top:2760px"></div>
<div class="abs foot-col" style="left:162px"><h5>Shop</h5><ul><li>Men Fashion</li><li>Women Fashion</li><li>Deals</li><li>Lookbook</li><li>Our Size Chart</li></ul></div>
<div class="abs foot-col" style="left:391px"><h5>Info</h5><ul><li>Order Status</li><li>Shipping Information</li><li>About Us</li><li>Store Locator</li><li>Contact Us</li></ul></div>
<div class="abs foot-col" style="left:593px"><h5>Customer services</h5><ul><li>Return Policy</li><li>Terms &amp; condition</li><li>Privacy Policy</li><li>FAQ</li></ul></div>
<div class="abs foot-col" style="left:839px"><h5>Follow us</h5>
  <div class="social">
    <span class="c1"><i></i>Friendnet</span><span class="c2"><i></i>Chirper</span>
    <span class="c3"><i></i>Snapgrid</span><span class="c4"><i></i>Vidstream</span>
  </div>
</div>

<div class="abs rule-inner" style="top:3017px"></div>
<div class="abs contact">
  <span><svg width="10" height="10" viewBox="0 0 10 10"><path d="M2 1l2 2-1 1a5 5 0 003 3l1-1 2 2-1 1C4 9 1 6 1 2z" fill="#333"/></svg>+11 - 555 - 0142 - 0000</span>
  <span><svg width="12" height="9" viewBox="0 0 12 9"><rect x="0.5" y="0.5" width="11" height="8" fill="#333"/><path d="M0.5 0.5L6 5l5.5-4.5" fill="none" stroke="#fff"/></svg>INFO@QUILLBARN7823.EXAMPLE</span>
</div>
<div class="abs rule-inner" style="top:3088px"></div>
<div class="abs pay"><i></i><i></i><i></i><i></i><i></i><i></i><i></i><i></i><i></i><i></i><i></i></div>

<footer class="abs bottom">© 2019 QuillBarn23' - All rights reserved</footer>

</body>
</html>
```